Nobre Lente Lusitana - business card

Create a business card for my eyewear (glasses) store. The concept is based in handcrafted glasses (as well as common frames and 3d printed), clean, and elegant. The business card could be black (white letters and symbols) or white (black letters and symbols) but we are open to new suggestions. It must be sober and elegant.
The name Nobre Lente Lusitana means Royal/Real Portuguese Optical Store.
Our concept should be inspired by the pictures attatched bellow.
I would like it to be classic and elegant as business cards for bankers.
Our first selected logo is also available in attachment files.

Target Market(s)

For business meetings with investors, supliers and fairs

Industry/Entity Type

Eyewear

Contact Information for Business Card

Some random business cards in attachment that we like. Don't be closed to it, we like freedom of think.

Font styles to use
Serif
Sans Serif

Colors
404040
e9e9e9
fbfbfb
000000
85abd3
0255a3
f7fbfd
959595

Requirements
Must have
• Must be elegant, simple.
• Must present our brand new logo (slight variations are welcome, the logo is not closed yet). See our temporary logo in attachment.
• Black (or dark grey), white (or light grey) and a third slight color.
• This third slight color could be dark blue or grayish blue.
• Info:
• Tomás Vidigal (name)
• tvidigal@nobrelentelusitana.example
• +351 927364051
• www.nobrelentelusitana.example
Nice to have
• Black and white or with serious colors such as dark blue or greyish blue.
• Could also have water mark with our logo (big size) in the background (inspired in KMT bank credit card design)
Should not have
• Hysteric colora or shapes

```html
<!DOCTYPE html>
<html lang="pt">
<head>
<meta charset="utf-8">
<title>Nobre Lente Lusitana – Cartão de visita</title>
<link rel="stylesheet" href="https://fonts.googleapis.com/css2?family=Jost:wght@400;500&family=Roboto+Slab:wght@700;800;900&family=Tinos:wght@700&display=swap">
<style>
  :root {
    --ink: #000000;
    --paper: #ffffff;
    --white: #fbfbfb;
    --art-light: #9a9a9a;
    --art-mid: #6b6b6b;
    --art-dark: #464646;
    --band-dark: #555555;
    --band-light: #7a7a7a;
    --watermark: #3c3c3c;
  }
  * { margin: 0; padding: 0; box-sizing: border-box; }
  html, body { width: 1200px; height: 1000px; overflow: hidden; background: var(--paper); }
  .canvas { position: relative; width: 1200px; height: 1000px; }

  .card { position: absolute; width: 637px; background: var(--ink); border-radius: 22px; overflow: hidden; }
  .card-front { left: 284px; top: 98px; height: 389px; }
  .card-back { left: 279px; top: 513px; height: 388px; }

  .band-dark { position: absolute; left: 0; right: 0; top: 340px; height: 22px; background: var(--band-dark); }
  .band-light { position: absolute; left: 0; right: 0; top: 362px; bottom: 0; background: var(--band-light); }

  .spectacles-art {
    position: absolute; left: 4px; top: 17px; width: 628px; height: 306px; border-radius: 153px;
    background: linear-gradient(180deg, var(--art-light) 0%, var(--art-mid) 45%, var(--art-dark) 100%);
  }

  .column { position: absolute; top: 0; height: 340px; text-align: center; color: var(--white); }
  .column-brand { left: 4px; width: 306px; }
  .column-contact { left: 324px; width: 306px; }

  .brand-name { font-family: "Jost", sans-serif; font-weight: 400; color: var(--white); line-height: 1; }
  .column-brand .brand-main { position: absolute; left: 0; right: 0; top: 212px; font-size: 28px; letter-spacing: 1.5px; }
  .column-brand .brand-sub { position: absolute; left: 0; right: 0; top: 246px; font-size: 17px; letter-spacing: 1.5px; }

  .person-name {
    position: absolute; left: -10px; right: -10px; top: 148px; line-height: 1;
    font-family: "Roboto Slab", serif; font-weight: 800; font-size: 25px;
    text-shadow: 3px 3px 0 rgba(0,0,0,.55);
  }
  .contact { position: absolute; left: 0; right: 0; line-height: 1; font-family: "Tinos", serif; font-weight: 700; }
  .contact-email { top: 192px; font-size: 13px; }
  .contact-web { top: 215px; font-size: 13px; }
  .contact-phone { top: 239px; font-size: 10.5px; }

  .wm-mark { position: absolute; width: 70px; height: 70px; border: 5px solid var(--watermark); border-radius: 50%; }
  .watermark { position: absolute; width: 200px; text-align: center; font-family: "Jost", sans-serif; font-weight: 400; color: var(--watermark); line-height: 1; }
  .watermark .wm-main { display: block; font-size: 24px; letter-spacing: 1.5px; }
  .watermark .wm-sub { display: block; font-size: 14px; letter-spacing: 1.5px; margin-top: 5px; }

  .brand-mark { position: absolute; left: 278px; top: 122px; width: 82px; height: 82px; border: 7px solid var(--white); border-radius: 50%; }
  .back-brand { position: absolute; left: 0; right: 0; top: 246px; text-align: center; }
  .back-brand .brand-main { display: block; font-size: 31px; letter-spacing: 2px; }
  .back-brand .brand-sub { display: block; font-size: 19px; letter-spacing: 2px; margin-top: 2px; }
  .back-web { position: absolute; left: 0; right: 0; top: 308px; text-align: center; font-family: "Tinos", serif; font-weight: 700; font-size: 15px; color: var(--white); }
</style>
</head>
<body>
<div class="canvas">

  <section class="card card-front" aria-label="Frente do cartão">
    <div class="band-dark"></div>
    <div class="band-light"></div>
    <div class="spectacles-art" role="img" aria-label="Ilustração de uns óculos redondos com aros metálicos"></div>

    <div class="column column-brand">
      <div class="brand-name brand-main">NOBRE LENTE</div>
      <div class="brand-name brand-sub">LUSITANA</div>
    </div>

    <div class="column column-contact">
      <div class="person-name">Tomás Vidigal</div>
      <div class="contact contact-email">tvidigal@nobrelentelusitana.example</div>
      <div class="contact contact-web">www.nobrelentelusitana.example</div>
      <div class="contact contact-phone">+351 927364051</div>
    </div>
  </section>

  <section class="card card-back" aria-label="Verso do cartão">
    <div class="wm-mark" style="left:73px; top:62px"></div>
    <div class="wm-mark" style="left:284px; top:62px"></div>
    <div class="wm-mark" style="left:496px; top:62px"></div>
    <div class="wm-mark" style="left:73px; top:238px"></div>
    <div class="wm-mark" style="left:284px; top:238px"></div>
    <div class="wm-mark" style="left:496px; top:238px"></div>

    <div class="watermark" style="left:8px; top:154px"><span class="wm-main">NOBRE LENTE</span><span class="wm-sub">LUSITANA</span></div>
    <div class="watermark" style="left:219px; top:154px"><span class="wm-main">NOBRE LENTE</span><span class="wm-sub">LUSITANA</span></div>
    <div class="watermark" style="left:431px; top:154px"><span class="wm-main">NOBRE LENTE</span><span class="wm-sub">LUSITANA</span></div>
    <div class="watermark" style="left:8px; top:331px"><span class="wm-main">NOBRE LENTE</span><span class="wm-sub">LUSITANA</span></div>
    <div class="watermark" style="left:219px; top:331px"><span class="wm-main">NOBRE LENTE</span><span class="wm-sub">LUSITANA</span></div>
    <div class="watermark" style="left:431px; top:331px"><span class="wm-main">NOBRE LENTE</span><span class="wm-sub">LUSITANA</span></div>

    <div class="brand-mark"></div>
    <div class="back-brand">
      <span class="brand-name brand-main">NOBRE LENTE</span>
      <span class="brand-name brand-sub">LUSITANA</span>
    </div>
    <div class="back-web">www.nobrelentelusitana.example</div>
  </section>

</div>
</body>
</html>
```